Business Card Design Project

We need a business card design for a new company based in Singapore called 'Bright Harbor Pte Ltd'. We provide personal development training and emotional intelligence workshops. Our slogan is "Actualize your potentials". We will not have a company address on the business card. Only phone number, email address and website address.

Target Market(s)

Adults age 25 to 45 years old.
Mostly working in a job.

Industry/Entity Type

Training

Colors
0255a2
f37123

```html
<!DOCTYPE html>
<html lang="en">
<head>
<meta charset="utf-8">
<title>Bright Harbor Pte Ltd — Business Card</title>
<link rel="stylesheet" href="https://fonts.googleapis.com/css2?family=Questrial&display=swap">
<style>
  :root {
    --navy: #1c315e;
    --orange: #f26722;
    --white: #ffffff;
    --page: #ffffff;
  }
  html, body {
    margin: 0;
    padding: 0;
    width: 1200px;
    height: 699px;
    overflow: hidden;
    background: var(--page);
  }
  .card {
    position: relative;
    width: 1200px;
    height: 699px;
    background: var(--white);
    font-family: "Questrial", "Helvetica Neue", Arial, sans-serif;
    overflow: hidden;
  }
  .contact-band {
    position: absolute;
    left: 0;
    top: 0;
    width: 1200px;
    height: 270px;
    background: var(--navy);
  }
  .accent-stripe {
    position: absolute;
    left: 0;
    top: 270px;
    width: 1200px;
    height: 26px;
    background: var(--orange);
  }
  .contact-list {
    margin: 0;
    padding: 0;
    list-style: none;
    color: var(--white);
  }
  .contact-list li {
    position: absolute;
    line-height: 1;
    white-space: nowrap;
    text-align: right;
  }
  .contact-phone {
    top: 38px;
    right: 20px;
    font-size: 50px;
    letter-spacing: 12px;
  }
  .contact-email {
    top: 114px;
    right: 26px;
    font-size: 40px;
    letter-spacing: 6px;
    text-transform: uppercase;
  }
  .contact-web {
    top: 183px;
    right: 27px;
    font-size: 40px;
    letter-spacing: 5px;
    text-transform: uppercase;
  }
  .brand {
    position: absolute;
    left: 300px;
    top: 420px;
    display: flex;
    align-items: center;
    gap: 26px;
  }
  .brand-mark {
    display: block;
    width: 160px;
    height: 160px;
  }
  .brand-name {
    font-size: 44px;
    color: var(--navy);
    letter-spacing: 1px;
    white-space: nowrap;
  }
</style>
</head>
<body>
  <main class="card">
    <div class="contact-band"></div>
    <div class="accent-stripe"></div>

    <ul class="contact-list">
      <li class="contact-phone">555.555.5555</li>
      <li class="contact-email">email@address.com</li>
      <li class="contact-web">www.webaddress.com</li>
    </ul>

    <div class="brand">
      <svg class="brand-mark" viewBox="0 0 160 160" aria-hidden="true">
        <circle cx="80" cy="80" r="74" fill="none" stroke="var(--navy)" stroke-width="10"/>
      </svg>
      <span class="brand-name">Bright Harbor Pte Ltd</span>
    </div>
  </main>
</body>
</html>
```